Marn-ridge Tide Harbor Custom Brokers Limited

Name: Dorvella Hastings
Title: Customs Broker
Address: Shop 9 Birchfield Commercial Complex
207-209 Harlow Road
Kingston 8
Telephone: (876)
Email: tideharborport@quillmail.example

```html
<!DOCTYPE html>
<html lang="en">
<head>
<meta charset="utf-8">
<title>Marn-ridge Tide Harbor Custom Brokers Limited – Business Card</title>
<link rel="stylesheet" href="https://fonts.googleapis.com/css2?family=Source+Sans+3:wght@400;600;700&display=swap">
<style>
  :root {
    --navy: #0f2c52;
    --gold: #e6a520;
    --paper: #f4f4f4;
    --ink: #1f1f1f;
    --backdrop: #e4e4e4;
    --white: #ffffff;
    --rule: #9a9a9a;
  }
  * { margin: 0; padding: 0; box-sizing: border-box; }
  html, body {
    width: 1200px; height: 960px; overflow: hidden;
    background: var(--backdrop);
    font-family: "Source Sans 3", "Source Sans Pro", Arial, sans-serif;
  }
  .card {
    position: absolute; left: 317px; width: 567px; height: 324px;
    overflow: hidden;
  }
  .card--front { top: 135px; background: var(--navy); }
  .card--back  { top: 509px; background: var(--paper); }

  .brand {
    position: absolute; left: 0; right: 0;
    display: flex; flex-direction: column; align-items: center; gap: 14px;
    text-align: center;
  }
  .card--front .brand { top: 88px; }
  .card--back .brand { top: 34px; }
  .brand__dot { width: 46px; height: 46px; border-radius: 50%; background: var(--gold); }
  .brand__name {
    width: 360px; font-size: 25px; line-height: 1.15; font-weight: 700;
    letter-spacing: 0.5px;
  }
  .card--front .brand__name { color: var(--white); }
  .card--back .brand__name { color: var(--navy); }

  .holder {
    position: absolute; right: 325px; top: 213px; text-align: right;
  }
  .holder__name { font-size: 18px; font-weight: 700; color: var(--navy); letter-spacing: 0.3px; }
  .holder__title { font-size: 14px; color: var(--gold); margin-top: 2px; }

  .contact {
    position: absolute; left: 260px; top: 184px;
    border-left: 1px solid var(--rule); padding-left: 16px;
    font-size: 14px; line-height: 19px; color: var(--ink);
    height: 104px;
  }
  .contact__lines { margin-bottom: 6px; }
  .contact__row { display: flex; align-items: center; gap: 5px; }
  .contact__row svg { width: 13px; height: 13px; flex: none; }

  .band { position: absolute; left: 0; bottom: 0; width: 567px; height: 45px; }
</style>
</head>
<body>
  <section class="card card--front">
    <div class="brand">
      <span class="brand__dot"></span>
      <p class="brand__name">Marn-ridge Tide Harbor Custom Brokers Limited</p>
    </div>
  </section>

  <section class="card card--back">
    <div class="brand">
      <span class="brand__dot"></span>
      <p class="brand__name">Marn-ridge Tide Harbor Custom Brokers Limited</p>
    </div>

    <div class="holder">
      <p class="holder__name">DORVELLA HASTINGS</p>
      <p class="holder__title">Customs Broker</p>
    </div>

    <div class="contact">
      <p class="contact__lines">Shop 9 Birchfield Commercial Complex<br>207-209 Harlow Road<br>Kingston 8</p>
      <p class="contact__row">
        <svg viewBox="0 0 24 24" aria-hidden="true"><path fill="#e6a520" d="M6.6 10.8a15 15 0 0 0 6.6 6.6l2.2-2.2a1 1 0 0 1 1-.25 11.4 11.4 0 0 0 3.6.57 1 1 0 0 1 1 1V20a1 1 0 0 1-1 1A17 17 0 0 1 3 4a1 1 0 0 1 1-1h3.5a1 1 0 0 1 1 1c0 1.25.2 2.45.57 3.57a1 1 0 0 1-.25 1z"/></svg>
        (876) 555-0142
      </p>
      <p class="contact__row">
        <svg viewBox="0 0 24 24" aria-hidden="true"><rect x="2" y="5" width="20" height="14" fill="none" stroke="#e6a520" stroke-width="2.2"/><path d="M2 6l10 7 10-7" fill="none" stroke="#e6a520" stroke-width="2.2"/></svg>
        tideharborport@quillmail.example
      </p>
    </div>

    <svg class="band" viewBox="0 0 567 45" preserveAspectRatio="none" aria-hidden="true">
      <path d="M0 10 Q283 30 567 10 L567 45 L0 45 Z" fill="var(--navy)"/>
      <path d="M0 8 Q283 32 567 12" fill="none" stroke="var(--gold)" stroke-width="3"/>
      <path d="M0 14 Q283 36 567 16" fill="none" stroke="var(--white)" stroke-width="2"/>
    </svg>
  </section>
</body>
</html>
```